Business Card for TVK, logo files already created

Please, can you assist with creating a Business card the TVK graphics which are already listed on www.brinmoretech.example
The business card should be modern and upmarket, textured designs are welcome. Please feel free to express yourself and be very bold with your design.

Target Market(s)

Cyber Security

Industry/Entity Type

Information Technology

Contact Information for Business Card

Company Name
Name
Title
Mobile
Fax or Tel
email
url

Font styles to use
Serif
Sans Serif

Colors
3277b5
85acd3
ffffff

```html
<!DOCTYPE html>
<html lang="en">
<head>
<meta charset="utf-8">
<title>TVK Business Card</title>
<link href="https://fonts.googleapis.com/css2?family=Montserrat:wght@500;800&family=Noto+Sans:wght@400;600&display=swap" rel="stylesheet">
<style>
  :root {
    --navy: #0b1534;
    --brand-blue: #2b3f93;
    --ink: #2b2b33;
    --rule: #3a3a44;
    --paper: #ffffff;
    --backdrop: #e9e7e2;
  }
  * { box-sizing: border-box; margin: 0; padding: 0; }
  html, body { width: 1200px; height: 1200px; overflow: hidden; }
  body {
    background: var(--backdrop);
    position: relative;
    font-family: "Noto Sans", sans-serif;
  }
  .card {
    position: absolute;
    width: 700px;
    height: 400px;
    box-shadow: 0 18px 40px rgba(0,0,0,0.22);
  }
  /* Front */
  .card--front {
    left: 90px; top: 120px;
    background: var(--navy);
    color: var(--paper);
  }
  .card--front .brand {
    position: absolute;
    left: 0; right: 0; top: 100px;
    text-align: center;
  }
  .brand__name {
    font-family: "Montserrat", sans-serif;
    font-weight: 800;
    font-size: 120px;
    line-height: 1;
    letter-spacing: 4px;
  }
  .brand__company {
    font-family: "Montserrat", sans-serif;
    font-weight: 800;
    font-size: 24px;
    letter-spacing: 3px;
    margin-top: 10px;
  }
  .brand__tagline {
    font-family: "Montserrat", sans-serif;
    font-weight: 500;
    font-size: 15px;
    letter-spacing: 2px;
    margin-top: 10px;
  }
  /* Back */
  .card--back {
    left: 410px; top: 640px;
    background: var(--paper);
    border-bottom: 12px solid var(--navy);
  }
  .card--back .brand {
    position: absolute;
    right: 48px; top: 30px;
    text-align: center;
    color: var(--brand-blue);
  }
  .card--back .brand__name { font-size: 84px; }
  .card--back .brand__company { font-size: 17px; letter-spacing: 2px; margin-top: 6px; }
  .card--back .brand__tagline { font-size: 11px; letter-spacing: 1.5px; margin-top: 6px; }
  .divider {
    position: absolute;
    left: 48px; right: 48px; top: 186px;
    height: 1px;
    background: var(--rule);
  }
  .contact {
    position: absolute;
    left: 48px; top: 200px;
    color: var(--ink);
  }
  .contact__name {
    font-weight: 600;
    font-size: 30px;
    color: var(--brand-blue);
    line-height: 1.1;
  }
  .contact__title { font-size: 16px; line-height: 1.3; margin: 2px 0 8px; }
  .contact__list { list-style: none; }
  .contact__item {
    display: flex; align-items: center; gap: 10px;
    font-size: 16px; line-height: 1.4;
  }
  .contact__item svg { width: 14px; height: 14px; fill: var(--brand-blue); flex: none; }
</style>
</head>
<body>
  <section class="card card--front" aria-label="Business card front">
    <div class="brand">
      <div class="brand__name">TVK</div>
      <div class="brand__company">BRINMORE TECH SOLUTIONS</div>
      <div class="brand__tagline">SECURE - FORWARD THINKING</div>
    </div>
  </section>

  <section class="card card--back" aria-label="Business card back">
    <div class="brand">
      <div class="brand__name">TVK</div>
      <div class="brand__company">BRINMORE TECH SOLUTIONS</div>
      <div class="brand__tagline">SECURE - FORWARD THINKING</div>
    </div>
    <div class="divider"></div>
    <div class="contact">
      <div class="contact__name">Rafi Okonkwo</div>
      <div class="contact__title">Manager &amp; CEO</div>
      <ul class="contact__list">
        <li class="contact__item">
          <svg viewBox="0 0 16 16" aria-hidden="true"><path d="M3 1l3 3-1.5 2a9 9 0 0 0 5.5 5.5L12 10l3 3-2 2C6 15 1 10 1 3z"/></svg>
          +789-555-010
        </li>
        <li class="contact__item">
          <svg viewBox="0 0 16 16" aria-hidden="true"><rect x="4" y="1" width="8" height="4"/><rect x="1" y="6" width="14" height="9" rx="1"/></svg>
          +651-555-024
        </li>
        <li class="contact__item">
          <svg viewBox="0 0 16 16" aria-hidden="true"><path d="M1 3h14v10H1z M1 3l7 6 7-6" stroke="#fff" stroke-width="1"/></svg>
          contact@brinmoretech.example
        </li>
        <li class="contact__item">
          <svg viewBox="0 0 16 16" aria-hidden="true"><circle cx="8" cy="8" r="7"/><path d="M1 8h14M8 1c-3 4-3 10 0 14M8 1c3 4 3 10 0 14" stroke="#fff" fill="none"/></svg>
          www.brinmoretech.example
        </li>
      </ul>
    </div>
  </section>
</body>
</html>
```